Tri fold brochure for construction company

Looking for a tri fold brochure which utilizes black, teal and white colors. Logo must be on main page (several files with Logo attached)
Inside brochure.
1st Page - 3D photo/sketch/drawing of a complete residential high rise building with windows, balconies and elements of concrete and bricks.
2nd Page - Text which will outline company's main activities. file with text is attached.
3rd Page - photo/sketch/drawing of underground parking garage which shows columns/beams/walls/ and garage entrance/exit ramp. Can be multiple photos.
Back of brochure
1st page - company logo
2nd page - please propose something.
3rd page - company message with address and contact info (to be provided)
Back ground color of brochure should complement our logo/photos/sketches/drawings.
Alternative design options are welcome.

```html
<!DOCTYPE html>
<html lang="en">
<head>
<meta charset="utf-8">
<title>Northstone Building Group – Tri-fold Brochure</title>
<link rel="stylesheet" href="https://fonts.googleapis.com/css2?family=Montserrat:wght@600;700;800&family=Open+Sans:wght@400;600;700&display=swap">
<style>
:root{
  --teal:#1aa59a;
  --teal-dark:#0f6f69;
  --teal-deep:#0b4d4a;
  --ink:#1d1f21;
  --charcoal:#2b2e31;
  --paper:#ffffff;
  --stage:#eceeef;
  --muted:#5b6366;
}
*{box-sizing:border-box;margin:0;padding:0}
html,body{width:673px;height:1200px;overflow:hidden;background:var(--stage);font-family:"Open Sans",Arial,sans-serif;color:var(--ink)}
.sheet{position:absolute;left:18px;width:637px;display:grid;grid-template-columns:repeat(3,1fr);background:var(--paper);box-shadow:0 3px 10px rgba(0,0,0,.22)}
.sheet--outside{top:27px;height:534px}
.sheet--inside{top:635px;height:532px}
.panel{position:relative;overflow:hidden}
.web-bar{position:absolute;left:0;right:0;bottom:0;height:20px;background:var(--teal);color:#fff;font-size:7px;font-weight:600;display:flex;align-items:center;justify-content:center;letter-spacing:.3px}
.photo{position:absolute;left:0;right:0}
.brand{display:flex;align-items:center;gap:7px}
.brand__mark{width:22px;height:22px;background:var(--teal);flex:none}
.brand__name{font-family:"Montserrat",Arial,sans-serif;font-weight:800;font-size:15px;line-height:1;letter-spacing:.5px}
.brand__name small{display:block;font-size:6px;letter-spacing:1.6px;margin-top:3px}
.label{font-family:"Montserrat",Arial,sans-serif;font-weight:800;color:#fff;letter-spacing:.5px}
p.body{font-size:6.6px;line-height:1.5;color:var(--muted)}

/* outside: about */
.about .photo{top:0;height:230px;background:linear-gradient(170deg,#cfdde0 0%,#9fb3b0 45%,#4f7a5a 80%,#3c5c40 100%)}
.about__label{position:absolute;left:12px;top:240px;background:var(--teal-deep);padding:5px 10px;font-size:12px}
.about p.body{position:absolute;left:14px;right:14px;top:276px}

/* outside: contact */
.contact{background:linear-gradient(180deg,var(--teal) 0%,var(--teal-dark) 100%);color:#fff}
.contact .brand{position:absolute;left:30px;top:72px;color:#fff}
.contact .brand__mark{background:#fff}
.contact__label{position:absolute;left:0;right:0;top:180px;text-align:center;font-size:10px}
.contact__list{position:absolute;left:0;right:0;top:200px;list-style:none;text-align:center;font-size:7px;line-height:1.9}
.contact__list svg{width:8px;height:8px;vertical-align:-1px;margin-right:4px}
.location-bar{position:absolute;left:0;right:0;top:312px;height:24px;background:var(--charcoal);display:flex;align-items:center;justify-content:center;gap:6px;font-size:11px}
.map{position:absolute;left:0;right:0;top:336px;bottom:20px;background:linear-gradient(160deg,#eef2f1,#d6dfdd)}
.contact .web-bar{background:var(--teal-deep)}

/* outside: cover */
.cover .photo{top:0;height:405px;background:linear-gradient(160deg,#e6e8e6 0%,#b9c2c4 40%,#3f8f92 70%,#23393d 100%)}
.cover__title{position:absolute;left:14px;top:414px;font-family:"Montserrat",Arial,sans-serif;font-weight:800;color:var(--teal);font-size:19px;line-height:1.05}
.cover p.body{position:absolute;left:14px;right:14px;top:462px;color:var(--charcoal)}

/* inside */
.tower .brand{position:absolute;left:14px;top:16px;color:var(--ink)}
.tower .brand__name{color:var(--ink)}
.tower .photo{top:62px;bottom:0;background:linear-gradient(180deg,#f4f6f6 0%,#d9dfdf 35%,#8f9a97 75%,#5b6b4f 100%)}
.services{padding:24px 10px 0 12px;border-left:3px solid var(--teal)}
.misc{padding:24px 12px 0 10px}
.section-head{display:flex;align-items:center;gap:5px;background:var(--teal);padding:3px 5px;margin-bottom:6px}
.section-head__icon{width:12px;height:12px;background:var(--teal-deep);flex:none}
.section-head .label{font-size:8.5px}
.list{list-style:none;font-size:6.3px;line-height:1.5;color:var(--charcoal)}
.list > li{font-weight:700;margin-top:2px}
.list > li::before{content:"• ";color:var(--teal)}
.list ul{list-style:none;padding-left:10px;font-weight:400;color:var(--muted)}
.list ul li::before{content:"– "}
.services .section-head + .list{margin-bottom:12px}
.misc .list > li{font-weight:400}
.gallery{position:absolute;left:0;right:0;top:150px;bottom:0;display:grid;grid-template-rows:105px 95px 1fr;gap:5px}
.gallery div:nth-child(1){background:linear-gradient(135deg,#1f2b2e,#7a8a5a,#2f3a3c)}
.gallery div:nth-child(2){background:linear-gradient(135deg,#d8c9a8,#8c7a5b,#cfd4d2)}
.gallery div:nth-child(3){background:linear-gradient(160deg,#e4e6e4,#a7aeb0,#4d5659)}
</style>
</head>
<body>

<section class="sheet sheet--outside">
  <div class="panel about">
    <div class="photo" role="img" aria-label="Residential building surrounded by trees"></div>
    <h2 class="label about__label">ABOUT US</h2>
    <p class="body">Lorem ipsum dolor sit amet, consectetur adipiscing elit, sed do eiusmod tempor incididunt ut labore et dolore magna aliqua. Ut enim ad minim veniam, quis nostrud exercitation ullamco laboris nisi ut aliquip ex ea commodo consequat. Duis aute irure dolor in reprehenderit in voluptate velit esse cillum dolore eu fugiat nulla pariatur. Excepteur sint occaecat cupidatat non proident, sunt in culpa qui officia deserunt mollit anim id est laborum. Sed ut perspiciatis unde omnis iste natus error sit voluptatem accusantium doloremque laudantium, totam rem aperiam, eaque ipsa quae ab illo inventore veritatis et quasi architecto beatae vitae dicta sunt explicabo. Nemo enim ipsam voluptatem quia voluptas sit aspernatur aut odit aut fugit.</p>
    <div class="web-bar">www.northstonebuild.com</div>
  </div>

  <div class="panel contact">
    <div class="brand">
      <span class="brand__mark"></span>
      <span class="brand__name">NORTHSTONE<small>BUILDING GROUP</small></span>
    </div>
    <h3 class="label contact__label">CONTACT</h3>
    <ul class="contact__list">
      <li><svg viewBox="0 0 10 10"><path d="M2 1h2l1 2-1.2 1a5 5 0 0 0 2.2 2.2L7 5l2 1v2c0 .6-.5 1-1 1A8 8 0 0 1 1 2c0-.5.4-1 1-1z" fill="#fff"/></svg>416-555-0192</li>
      <li><svg viewBox="0 0 10 10"><rect x="1" y="2" width="8" height="6" fill="none" stroke="#fff"/><path d="M1 2l4 3 4-3" fill="none" stroke="#fff"/></svg>info@northstonebuild.com</li>
      <li>120 Harbour Lane, Suite 4</li>
      <li>Lakeview, ON L4Z 0A1</li>
    </ul>
    <div class="location-bar label">
      <svg width="10" height="12" viewBox="0 0 10 12"><path d="M5 0a4 4 0 0 1 4 4c0 3-4 8-4 8S1 7 1 4a4 4 0 0 1 4-4z" fill="#fff"/><circle cx="5" cy="4" r="1.5" fill="#2b2e31"/></svg>
      LOCATION
    </div>
    <div class="map" role="img" aria-label="Street map showing the office location"></div>
    <div class="web-bar">www.northstonebuild.com</div>
  </div>

  <div class="panel cover">
    <div class="photo" role="img" aria-label="Modern interior with teal and grey finishes"></div>
    <h1 class="cover__title">LOREM IPSUM<br>DOLOR SIT AMET</h1>
    <p class="body">Consectetur adipiscing elit, sed do eiusmod tempor incididunt ut labore et dolore magna aliqua, ut enim ad minim veniam.</p>
    <div class="web-bar">www.northstonebuild.com</div>
  </div>
</section>

<section class="sheet sheet--inside">
  <div class="panel tower">
    <div class="brand">
      <span class="brand__mark"></span>
      <span class="brand__name">NORTHSTONE<small>BUILDING GROUP</small></span>
    </div>
    <div class="photo" role="img" aria-label="Residential high-rise with balconies and green glass"></div>
  </div>

  <div class="panel services">
    <div class="section-head"><span class="section-head__icon"></span><h3 class="label">BUILDING ENVELOPE:</h3></div>
    <ul class="list">
      <li>Concrete repairs<ul><li>Slab repairs</li><li>Wall repairs</li><li>Beams &amp; columns</li></ul></li>
      <li>Masonry repairs<ul><li>Brick &amp; stone replacement</li><li>Joint repointing</li><li>Lintel replacement</li><li>Parapet rebuilding</li></ul></li>
      <li>Sealant Replacement<ul><li>Window and door perimeter sealant</li><li>Control joints</li><li>Masonry sealants</li></ul></li>
      <li>Waterproofing<ul><li>Balcony &amp; terrace coatings</li><li>Roof membranes</li></ul></li>
    </ul>
    <div class="section-head"><span class="section-head__icon"></span><h3 class="label">PARKING GARAGE STRUCTURES:</h3></div>
    <ul class="list">
      <li>Concrete repairs<ul><li>Ramp and slab repairs</li><li>Column and beam repairs</li><li>Traffic coatings</li><li>Expansion joints</li><li>Crack injection</li></ul></li>
      <li>Waterproofing<ul><li>Membrane over occupied space</li><li>Hot applied systems</li><li>Drainage upgrades</li><li>Foundation wall repairs</li></ul></li>
      <li>Ramp Protection<ul><li>Heated ramp systems</li><li>Line painting &amp; signage</li></ul></li>
    </ul>
  </div>

  <div class="panel misc">
    <div class="section-head"><span class="section-head__icon"></span><h3 class="label">MISCELLANEOUS</h3></div>
    <ul class="list">
      <li>Railings installation and repair</li>
      <li>Exterior painting</li>
      <li>Window and door replacement</li>
      <li>Shotcrete and caulking</li>
      <li>Demolition and site work</li>
      <li>Snow melting systems</li>
      <li>Lintel repairs</li>
      <li>Fire stopping</li>
    </ul>
    <div class="gallery">
      <div role="img" aria-label="Underground parking garage with columns and beams"></div>
      <div role="img" aria-label="Garage entrance ramp"></div>
      <div role="img" aria-label="Concrete parking level with painted lines"></div>
    </div>
  </div>
</section>

</body>
</html>
```